Beautiful Simple and Clean WEbsite for Life Coach

Looking for a simple clean site website for life coach for educators. A home page will have an embedded opt-in form, menu bar will be
Work With Me - page for my coaching program and link to online calendar for booking
PRAISE - testimonials
ABOUT
PODCAST
I can supply images and a site I would like it modeled after is https://tessabrook.com/
My current website at www.danawhitfield.com is too dark. I am looking for the white space, pink and magenta. Feel free to use images from the site

Industry/Entity Type

Life Coaching

Number of Pages Required

4 page

Font styles to use
Serif

Colors
E54698
E96AAD
F1A4CE
F9D9EA
FCEFF6

Requirements
Must have
• See attached files for must-haves, Lots of white space, opt-in from for freebie is the most prominent on home page
Nice to have
• refer to Tessa Brook websites
Should not have
• dark colors, any balck background

```html
<!DOCTYPE html>
<html lang="en">
<head>
<meta charset="utf-8">
<title>Dana Whitfield – Life Coach for Educators</title>
<link href="https://fonts.googleapis.com/css2?family=Great+Vibes&family=Roboto:wght@400;500;700&display=swap" rel="stylesheet">
<style>
:root{
  --mauve:#9c7d88;
  --mauve-dark:#8a6b76;
  --pink:#ffc9d5;
  --pink-soft:#ffebef;
  --pink-hero:#fde3e8;
  --ink:#1f1a1c;
  --text:#5d5558;
  --white:#ffffff;
  --line:#eadde1;
}
*{box-sizing:border-box;margin:0;padding:0}
html,body{width:1200px;height:3095px;overflow:hidden}
body{position:relative;font-family:"Roboto",sans-serif;color:var(--text);background:var(--white)}
.script{font-family:"Great Vibes",cursive;font-weight:400;color:var(--ink)}
.btn{display:inline-flex;align-items:center;gap:10px;background:var(--mauve);color:var(--white);font-weight:700;font-size:14px;text-transform:uppercase;border-radius:30px;text-decoration:none;letter-spacing:.2px}
.divider{display:flex;align-items:center;gap:5px;margin-top:6px}
.divider i{display:block;border-radius:50%;background:var(--mauve)}
.photo{position:absolute}

/* header */
.site-header{position:absolute;left:0;top:0;width:1200px;height:64px;background:var(--mauve)}
.brand{position:absolute;left:111px;top:20px;color:var(--white);font-size:20px;font-weight:500}
.nav{position:absolute;left:500px;top:24px;display:flex;gap:46px}
.nav a{color:var(--white);font-weight:700;font-size:15px;text-decoration:none}
.search{position:absolute;left:1037px;top:14px;width:38px;height:38px;border-radius:50%;background:var(--pink);display:flex;align-items:center;justify-content:center}

/* hero */
.hero-bg{position:absolute;left:402px;top:64px;width:798px;height:556px;background:var(--pink-hero)}
.hero-photo{left:630px;top:88px;width:495px;height:532px;background:linear-gradient(180deg,#c9a772 0%,#d8c7b6 25%,#7d8f9e 55%,#3f5467 100%);border-radius:240px 240px 0 0}
.hero-card{position:absolute;left:111px;top:154px;width:463px;height:377px;background:var(--pink);border:8px solid var(--mauve)}
.hero-card h1{position:absolute;left:42px;top:38px;font-size:50px}
.hero-card p{position:absolute;left:44px;top:118px;font-size:18px;font-weight:500;color:var(--ink);line-height:26px}
.hero-card .btn{position:absolute;left:44px;top:292px;height:48px;padding:0 28px}

/* about */
.about-ring{position:absolute;left:114px;top:716px;width:454px;height:466px;border-radius:50%;background:var(--pink)}
.about-frame{position:absolute;left:114px;top:714px;width:452px;height:452px;border-radius:50%;background:var(--mauve)}
.about-photo{left:126px;top:734px;width:428px;height:428px;border-radius:50%;background:linear-gradient(160deg,#c8b79c,#e9e2d9 55%,#b9a58a)}
.about-text{position:absolute;left:645px;top:718px;width:444px}
.about-text h2{font-size:46px;line-height:52px}
.about-text h3{margin-top:18px;font-size:22px;font-weight:500;color:var(--mauve)}
.about-text p{margin-top:18px;font-size:14.5px;line-height:24px;text-align:justify}
.about-text .btn{margin-top:24px;height:48px;padding:0 28px}

/* work */
.work{position:absolute;left:0;top:1278px;width:1200px;height:557px;background:var(--pink-soft)}
.work-text{position:absolute;left:112px;top:70px;width:446px}
.work-text h2{font-size:46px;line-height:52px}
.work-text p{margin-top:18px;font-size:14.5px;line-height:24px;text-align:justify}
.work-text .btn{margin-top:24px;height:48px;padding:0 30px}
.work-photo{left:661px;top:63px;width:427px;height:434px;background:linear-gradient(160deg,#f3ede8,#e8c9d2 50%,#b9c2cf)}

/* blog */
.blog-title{position:absolute;left:0;top:1905px;width:1200px;text-align:center}
.blog-title h2{font-size:46px;line-height:52px}
.blog-title .divider{justify-content:center}
.card{position:absolute;top:2016px;width:316px;height:382px;border:1px solid var(--line);border-radius:6px;background:var(--white);overflow:hidden}
.card .thumb{position:relative;height:206px}
.date{position:absolute;left:0;bottom:0;width:62px;height:62px;background:var(--mauve);color:var(--white);text-align:center;padding-top:9px}
.date b{display:block;font-size:22px;font-weight:500;line-height:22px}
.date span{font-size:13px;font-weight:500}
.card h4{margin:24px 20px 0;font-size:16px;font-weight:700;color:var(--ink)}
.card hr{margin:10px 20px 0;width:30px;border:0;border-top:3px solid var(--mauve)}
.card p{margin:14px 20px 0;font-size:14.5px;line-height:22px}
.card .btn{margin:14px 0 0 21px;height:34px;padding:0 21px;font-size:12px}

/* contact */
.contact{position:absolute;left:0;top:2498px;width:1200px;height:550px;background:linear-gradient(180deg,#ffc9d5,#f8bcc9)}
.contact-title{position:absolute;left:0;top:60px;width:1200px;text-align:center}
.contact-title h2{font-size:46px;line-height:52px}
.contact-title .divider{justify-content:center}
.contact-title p{margin-top:40px;font-size:14px}
.contact-title p b{color:var(--ink);font-weight:500}
.info{position:absolute;left:106px;display:flex;gap:24px}
.info .ico{width:50px;height:50px;border-radius:50%;background:var(--white);display:flex;align-items:center;justify-content:center}
.info h5{font-size:14px;font-weight:700;color:var(--ink);margin-top:4px}
.info p{font-size:14px;line-height:22px;color:var(--mauve-dark);margin-top:6px}
.field{position:absolute;width:316px;height:50px;background:var(--white);border:1px solid var(--line);display:flex;align-items:center;justify-content:space-between;padding:0 18px;font-size:14px;color:#6f6669}
.message{position:absolute;left:777px;top:252px;width:316px;height:170px;background:var(--white);border:1px solid var(--line);padding:18px;display:flex;justify-content:space-between;font-size:14px;color:#6f6669}
.contact .submit{position:absolute;left:777px;top:448px;height:48px;padding:0 26px}

/* footer */
.site-footer{position:absolute;left:0;top:3048px;width:1200px;height:47px;background:var(--mauve);color:var(--white);font-size:14px}
.legal{position:absolute;left:106px;top:15px;display:flex;gap:20px}
.copy{position:absolute;right:112px;top:15px}
</style>
</head>
<body>

<header class="site-header">
  <div class="brand">Dana Whitfield</div>
  <nav class="nav"><a href="#">Home</a><a href="#">Work With Me</a><a href="#">Praise</a><a href="#">About</a><a href="#">Podcast</a></nav>
  <div class="search"><svg width="14" height="14" viewBox="0 0 14 14"><circle cx="6" cy="6" r="4.2" fill="none" stroke="#fff" stroke-width="2"/><path d="M9 9l4 4" stroke="#fff" stroke-width="2"/></svg></div>
</header>

<section class="hero">
  <div class="hero-bg"></div>
  <div class="photo hero-photo" role="img" aria-label="Portrait of the coach in a wide straw hat and denim jacket"></div>
  <div class="hero-card">
    <h1 class="script">Life Coach for Educators</h1>
    <p>Being Overworked<br>Being Overwhelmed<br>and not having Work - Life Balance<br><br>Who are OVER...<br>and Want LESS Stress</p>
    <a class="btn" href="#">Let me tell you more</a>
  </div>
</section>

<section class="about">
  <div class="about-ring"></div>
  <div class="about-frame"></div>
  <div class="photo about-photo" role="img" aria-label="Smiling coach in a white shirt sitting in tall dry grass"></div>
  <div class="about-text">
    <h2 class="script">About Me</h2>
    <div class="divider"><svg width="17" height="15" viewBox="0 0 17 15"><path d="M8.5 15L1.3 7.8A4.2 4.2 0 018.5 2a4.2 4.2 0 017.2 5.8z" fill="#9c7d88"/></svg><i style="width:8px;height:8px;margin-left:5px"></i><i style="width:6px;height:6px"></i><i style="width:4px;height:4px"></i></div>
    <h3>Hi, I'm Dana Whitfield</h3>
    <p>I'm a Life Coach. &nbsp;I am also a retired Elementary School Principal who loves other educators and everything in education.</p>
    <p>In my coaching practice, I empower my clients with simple survival skills to succeed at their school and in their life. &nbsp;They have more time, less stress, and yell less.</p>
    <p>If you would like to learn more about how to manage stress and overwhelm, and how to feel better no matter what the circumstances I am your gal.</p>
    <a class="btn" href="#">Opt in page <svg width="14" height="14" viewBox="0 0 14 14"><circle cx="7" cy="7" r="7" fill="#fff"/><path d="M5.5 4l3 3-3 3" stroke="#9c7d88" stroke-width="2" fill="none"/></svg></a>
  </div>
</section>

<section class="work">
  <div class="work-text">
    <h2 class="script">Work With Me</h2>
    <div class="divider"><svg width="17" height="15" viewBox="0 0 17 15"><path d="M8.5 15L1.3 7.8A4.2 4.2 0 018.5 2a4.2 4.2 0 017.2 5.8z" fill="#9c7d88"/></svg><i style="width:8px;height:8px;margin-left:5px"></i><i style="width:6px;height:6px"></i><i style="width:4px;height:4px"></i></div>
    <p>Sed ut perspiciatis unde omnis iste natus error sit voluptatem accusantium doloremque laudantium, totam rem aperiam, eaque ipsa quae ab illo inventore veritatis et quasi architecto beatae vitae dicta sunt explicabo. Nemo enim ipsam voluptatem quia voluptas sit aspernatur aut odit aut fugit, sed quia consequuntur magni dolores eos qui ratione voluptatem sequi nesciunt. Neque porro quisquam est, qui dolorem ipsum quia dolor sit amet, consectetur, adipisci velit, sed quia non numquam eius modi tempora incidunt ut labore et dolore magnam aliquam quaerat voluptatem. Ut enim ad minima veniam, quis nostrum exercitationem ullam</p>
    <a class="btn" href="#">Schedule now <svg width="14" height="14" viewBox="0 0 14 14"><rect x="1" y="2.5" width="12" height="10.5" fill="none" stroke="#fff" stroke-width="1.6"/><path d="M1 6h12M4 1v3M10 1v3" stroke="#fff" stroke-width="1.6"/></svg></a>
  </div>
  <div class="photo work-photo" role="img" aria-label="Thoughtful woman in a pink sweater sitting on the floor with a laptop"></div>
</section>

<section class="blog">
  <div class="blog-title">
    <h2 class="script">Latest Blog</h2>
    <div class="divider"><svg width="17" height="15" viewBox="0 0 17 15"><path d="M8.5 15L1.3 7.8A4.2 4.2 0 018.5 2a4.2 4.2 0 017.2 5.8z" fill="#9c7d88"/></svg><i style="width:8px;height:8px;margin-left:5px"></i><i style="width:6px;height:6px"></i><i style="width:4px;height:4px"></i></div>
  </div>
  <article class="card" style="left:106px">
    <div class="thumb" role="img" aria-label="Laughing woman with windswept blond hair outdoors" style="background:linear-gradient(160deg,#5e5f4a,#d9c4a0 55%,#e7b75a)"><div class="date"><b>10</b><span>OCT</span></div></div>
    <h4>Sed ut perspiciatis unde omnis</h4><hr>
    <p>Ut enim ad minima veniam, quis nostrum exercitationem ullam corporis</p>
    <a class="btn" href="#">Read more</a>
  </article>
  <article class="card" style="left:443px">
    <div class="thumb" role="img" aria-label="Woman stretching on a beach at sunset" style="background:linear-gradient(160deg,#c98a78,#f4e1cf 50%,#8fa3b3)"><div class="date"><b>10</b><span>OCT</span></div></div>
    <h4>Sed ut perspiciatis unde omnis</h4><hr>
    <p>Ut enim ad minima veniam, quis nostrum exercitationem ullam corporis</p>
    <a class="btn" href="#">Read more</a>
  </article>
  <article class="card" style="left:780px">
    <div class="thumb" role="img" aria-label="Person meditating on a deck at sunrise" style="background:linear-gradient(180deg,#8c7a66,#c9a680 45%,#3b3029)"><div class="date"><b>10</b><span>OCT</span></div></div>
    <h4>Sed ut perspiciatis unde omnis</h4><hr>
    <p>Ut enim ad minima veniam, quis nostrum exercitationem ullam corporis</p>
    <a class="btn" href="#">Read more</a>
  </article>
</section>

<section class="contact">
  <div class="contact-title">
    <h2 class="script">Get In Touch</h2>
    <div class="divider"><svg width="17" height="15" viewBox="0 0 17 15"><path d="M8.5 15L1.3 7.8A4.2 4.2 0 018.5 2a4.2 4.2 0 017.2 5.8z" fill="#9c7d88"/></svg><i style="width:8px;height:8px;margin-left:5px"></i><i style="width:6px;height:6px"></i><i style="width:4px;height:4px"></i></div>
    <p>I would love to hear from you! Simply fill out the form or email <b>dana@danawhitfield.com</b> and I'll get back to you.</p>
  </div>

  <div class="info" style="top:276px">
    <div class="ico"><svg width="20" height="24" viewBox="0 0 20 24"><path d="M10 23s8-8 8-13a8 8 0 00-16 0c0 5 8 13 8 13z" fill="none" stroke="#f0a9ba" stroke-width="1.5"/><circle cx="10" cy="10" r="3" fill="none" stroke="#f0a9ba" stroke-width="1.5"/></svg></div>
    <div><h5>LOCATION</h5><p style="font-weight:500">27 Linden Row, Ashfield MA<br>United States</p></div>
  </div>
  <div class="info" style="top:368px">
    <div class="ico"><svg width="24" height="20" viewBox="0 0 24 20"><rect x="2" y="4" width="20" height="14" fill="none" stroke="#f0a9ba" stroke-width="1.5"/><path d="M2 4l10 8 10-8" fill="none" stroke="#f0a9ba" stroke-width="1.5"/></svg></div>
    <div><h5>EMAIL US</h5><p style="margin-top:2px">dana@danawhitfield.com</p></div>
  </div>
  <div class="info" style="top:442px">
    <div class="ico"><svg width="22" height="22" viewBox="0 0 22 22"><path d="M5 2l4 4-2 3c1 3 3 5 6 6l3-2 4 4-3 3C9 19 3 13 2 5z" fill="none" stroke="#f0a9ba" stroke-width="1.5"/></svg></div>
    <div><h5>CONTACT US</h5><p style="margin-top:2px;font-size:16px;font-weight:500">+ 1 555 014 2290</p></div>
  </div>

  <div class="field" style="left:437px;top:252px">First Name <svg width="13" height="13" viewBox="0 0 13 13"><circle cx="6.5" cy="6.5" r="5.8" fill="none" stroke="#555" stroke-width="1.2"/><circle cx="6.5" cy="5" r="2" fill="#555"/><path d="M3 10.5a4 3 0 017 0" fill="#555"/></svg></div>
  <div class="field" style="left:437px;top:312px">Email <svg width="14" height="11" viewBox="0 0 14 11"><rect x="1" y="1" width="12" height="9" fill="none" stroke="#555" stroke-width="1.2"/><path d="M1 1l6 5 6-5" fill="none" stroke="#555" stroke-width="1.2"/></svg></div>
  <div class="field" style="left:437px;top:372px">Phone No <svg width="12" height="12" viewBox="0 0 22 22"><path d="M5 2l4 4-2 3c1 3 3 5 6 6l3-2 4 4-3 3C9 19 3 13 2 5z" fill="#555"/></svg></div>
  <div class="field" style="left:437px;top:432px">Post Code <svg width="10" height="13" viewBox="0 0 20 24"><path d="M10 23s8-8 8-13a8 8 0 00-16 0c0 5 8 13 8 13z" fill="#555"/><circle cx="10" cy="10" r="3" fill="#fff"/></svg></div>
  <div class="message">Message <svg width="15" height="12" viewBox="0 0 15 12"><ellipse cx="6" cy="5" rx="5" ry="3.6" fill="none" stroke="#555" stroke-width="1.2"/><path d="M9 9.5c2 1 4 .5 5-.5" fill="none" stroke="#555" stroke-width="1.2"/></svg></div>
  <a class="btn submit" href="#">Submit now <svg width="14" height="14" viewBox="0 0 14 14"><circle cx="7" cy="7" r="7" fill="#fff"/><path d="M5.5 4l3 3-3 3" stroke="#9c7d88" stroke-width="2" fill="none"/></svg></a>
</section>

<footer class="site-footer">
  <div class="legal"><span>Disclaimer</span><span>|</span><span>Privacy Policy</span><span>|</span><span>Terms Of Use</span></div>
  <div class="copy">© 2022 Dana Whitfield. All Rights Reserved</div>
</footer>

</body>
</html>
```